Web Design + logo Project

hi,
we are based in ASEAN region (Malaysia/Indonesia/Singapore), involving in Online Vehicle Insurance Portal. so far our product is only car insurance and personal insurance, and motorbikes insurance)
We need a webdesign + logo for TolaKover.com
The website is www.tolakover.example. The website is already up with the necessary quotation comparison + purchase mechanism.
We like www.brightlane.example look and feel very much.
Blue is the preferred main theme.
The mainpage should highlight the following
1) quotation generator/input
2) hotline number
3) news/testimonial
The webdesign should be able to cater for mobile users as well.
The design should be professional and energetic
Target Market(s)
20-35years old vehicle owners in Indonesia/thailand/Singapore/vietnam
Industry/Entity Type
Car Insurance
Look and feel

```html
<!DOCTYPE html>
<html lang="en">
<head>
<meta charset="utf-8">
<title>TolaKover.com – Auto Insurance</title>
<link href="https://fonts.googleapis.com/css2?family=Arimo:wght@400;700&family=Roboto+Slab:wght@400;700;800&display=swap" rel="stylesheet">
<style>
:root{
  --blue:#0e4288;
  --blue-dark:#0b3470;
  --blue-deep:#082c5e;
  --blue-hero:#1a5bb0;
  --orange:#f7931e;
  --orange-light:#fbaa3c;
  --grey-bg:#f4f4f4;
  --text:#555;
  --link-blue:#1a4f95;
  --white:#fff;
}
*{margin:0;padding:0;box-sizing:border-box}
html,body{width:1129px;height:1200px;overflow:hidden}
body{font-family:"Arimo",Arial,sans-serif;background:var(--grey-bg);position:relative;color:var(--text)}
.abs{position:absolute}
a{color:inherit;text-decoration:none}

/* top bar */
.topbar{left:0;top:0;width:1129px;height:33px;background:var(--blue)}
.search{left:75px;top:6px;width:188px;height:21px;background:#fff;border:1px solid #ccd;display:flex}
.search span{flex:1;font-size:11px;color:#777;padding:4px 5px}
.search i{width:24px;border-left:1px solid #ccd;display:flex;align-items:center;justify-content:center}
.toplinks{right:54px;top:10px;font-size:12px;color:#fff}
.toplinks a+a::before{content:"|";color:#6d8fc0;margin:0 5px}

/* header */
.header{left:0;top:33px;width:1129px;height:95px;background:linear-gradient(#fafafa,#e9e9e9)}
.brand{left:75px;top:70px;display:flex;align-items:center;gap:8px;font-family:"Roboto Slab",serif;font-weight:800;font-size:25px;color:var(--blue)}
.brand b{width:14px;height:14px;background:var(--orange);border-radius:50%}
.mainnav{right:54px;top:72px;font-family:"Roboto Slab",serif;font-size:18px;color:var(--blue)}
.mainnav a{padding:0 12px;border-left:1px solid #bbb}
.mainnav a:first-child{border:0;color:var(--orange)}
.mainnav a:last-child{padding-right:0}

/* hero */
.hero{left:0;top:128px;width:1129px;height:303px;background:radial-gradient(ellipse at 55% 50%,#2a6cc2,var(--blue) 75%)}
.band{left:0;top:431px;width:1129px;height:70px;background:linear-gradient(var(--orange-light),var(--orange))}
.headline{left:393px;top:228px;color:#fff;font-family:"Roboto Slab",serif;font-weight:800;line-height:1}
.headline .h1{font-size:52px;letter-spacing:-1px}
.headline .sub{font-size:13px;font-weight:700;margin-top:-4px}
.headline .h2{font-size:34px;margin-top:-2px;padding-left:55px}
.photo{left:815px;top:140px;width:245px;height:291px;border-radius:110px 110px 0 0;background:linear-gradient(#f4d6c2,#e9b9c6 60%,#d3a0b8)}
.hotline{right:54px;top:443px;color:#fff;display:flex;align-items:baseline;gap:6px}
.hotline small{font-size:13px;font-weight:700}
.hotline strong{font-size:48px;font-family:"Arimo",sans-serif;letter-spacing:-2px}

/* quote form */
.quote{left:75px;top:170px;width:296px;height:306px;background:linear-gradient(#fff,#e8e8e8);box-shadow:0 2px 8px rgba(0,0,0,.35);padding:12px 9px}
.quote h2{font-family:"Roboto Slab",serif;font-weight:400;color:var(--orange);font-size:25px;text-align:center;margin-bottom:6px}
.field{height:39px;background:#fff;border:1px solid #ccc;margin-bottom:6px;font-size:17px;color:#888;padding:8px 11px}
.opt{display:flex;align-items:center;font-size:11px;color:#333;height:26px}
.opt label{font-family:"Roboto Slab",serif;font-size:16px;width:91px}
.radio{width:12px;height:12px;border:1px solid #999;border-radius:50%;margin:0 4px 0 0;background:#fff;display:inline-flex;align-items:center;justify-content:center}
.radio.on::after{content:"";width:4px;height:4px;border-radius:50%;background:#333}
.opt span+.radio{margin-left:7px}
.cta{margin-top:14px;height:48px;border-radius:4px;background:linear-gradient(#1d5aa8,var(--blue-dark));color:#fff;font-family:"Roboto Slab",serif;font-weight:700;font-size:21px;display:flex;align-items:center;justify-content:center;letter-spacing:-.5px}

/* intro */
.intro{left:78px;top:537px;width:960px}
.intro h2{font-family:"Roboto Slab",serif;font-weight:400;font-size:28px;color:var(--blue);letter-spacing:-1px;margin-bottom:10px}
.intro p{font-size:12px;line-height:16.5px;color:var(--link-blue)}
.rule{left:75px;top:667px;width:981px;border-top:1px dashed #aaa}

/* testimonials & news */
.sec-title{font-family:"Roboto Slab",serif;font-weight:800;font-size:45px;color:var(--blue);letter-spacing:-2px}
.sec-title em{font-style:normal;color:var(--orange)}
.testi-title{left:73px;top:703px}
.news-title{left:720px;top:703px}
.vline{left:686px;top:705px;height:225px;border-left:1px dotted #aaa}
.avatar{left:79px;top:785px;width:129px;height:120px;border:4px solid #ddd;outline:1px dashed #bbb;background:linear-gradient(#eef1f4,#c9d0d8)}
.quote-text{left:224px;top:785px;width:450px;font-size:12px;line-height:14.5px;color:#666}
.person{left:224px;top:860px;color:var(--blue);font-size:17px}
.person small{display:block;color:var(--orange);font-size:12px;font-weight:700;margin-top:2px}
.more{font-size:11px;font-weight:700;color:var(--blue);border-bottom:1px solid var(--blue)}
.more-t{left:595px;top:899px}
.more-n{left:969px;top:902px}
.news{left:722px;width:315px;font-size:12px;color:var(--link-blue)}
.news time{display:block;color:var(--orange);font-size:13px;font-family:"Roboto Slab",serif}
.news u{display:inline-block}
.n1{top:774px;padding-bottom:12px;border-bottom:1px dotted #aaa}
.n2{top:842px}

/* footer */
.foot-band{left:0;top:950px;width:1129px;height:36px;background:linear-gradient(var(--orange-light),var(--orange))}
.foot-body{left:0;top:986px;width:1129px;height:178px;background:var(--blue)}
.foot-bottom{left:0;top:1164px;width:1129px;height:36px;background:var(--blue-deep);color:#fff;font-size:11px;display:flex;justify-content:space-between;align-items:center;padding:0 54px 0 74px}
.col-h{top:958px;color:#fff;font-family:"Roboto Slab",serif;font-size:19px;letter-spacing:-1px}
.col{top:1003px;list-style:none;color:#fff;font-size:12px;line-height:19px}
.col li::before{content:"";display:inline-block;border-left:7px solid #fff;border-top:4px solid transparent;border-bottom:4px solid transparent;margin-right:6px}
.sep{top:1003px;height:130px;border-left:1px dotted #5b80b8}
</style>
</head>
<body>

<div class="abs topbar"></div>
<div class="abs search"><span>Search Keyword</span><i><svg width="14" height="14" viewBox="0 0 14 14"><circle cx="6" cy="6" r="4.5" fill="none" stroke="#2a78c8" stroke-width="1.6"/><line x1="9.3" y1="9.3" x2="13" y2="13" stroke="#2a78c8" stroke-width="1.8"/></svg></i></div>
<nav class="abs toplinks"><a>About</a><a>Careers</a><a>Contact</a><a>Login</a></nav>

<header class="abs header"></header>
<div class="abs brand"><b></b>TolaKover.com</div>
<nav class="abs mainnav"><a>Insurance Choice</a><a>Claims Center</a><a>Customer Service</a></nav>

<section class="abs hero"></section>
<div class="abs photo" role="img" aria-label="Photo of a smiling young woman holding up car keys"></div>
<div class="abs headline">
  <div class="h1">AutoInsurance</div>
  <div class="sub">ENJOY OUR CONCIERGE LEVEL OF CLAIMS SERVICE &amp;</div>
  <div class="h2">24-HOUR SUPPORT.</div>
</div>
<div class="abs band"></div>
<div class="abs hotline"><small>CALL US TODAY:</small><strong>0800-555-0199</strong></div>

<form class="abs quote">
  <h2>CHECK PREMIUMS</h2>
  <div class="field">Type of Vehicle:</div>
  <div class="field">Year:</div>
  <div class="field">Price Assured:</div>
  <div class="opt"><label>Category:</label><i class="radio on"></i><span>Personal</span><i class="radio"></i><span>Service</span></div>
  <div class="opt"><label>Coverage:</label><i class="radio on"></i><span>Total Loss Only</span><i class="radio"></i><span>Comprehensive</span></div>
  <div class="cta">CHECK THE QUOTATION</div>
</form>

<section class="abs intro">
  <h2>We’re Here 24/7. Call 1-800-TolaKover</h2>
  <p>Lorem ipsum dolor sit amet, consectetuer adipiscing elit, sed diam nonummy nibh euismod tincidunt ut laoreet dolore magna aliquam erat volutpat. Ut wisi enim ad minim veniam, quis nostrud exerci tation ullamcorper suscipit lobortis nisl ut aliquip ex ea commodo consequat. Duis autem vel eum iriure dolor in hendrerit in vulputate velit esse molestie consequat, vel illum dolore eu feugiat nulla facilisis at vero eros et accumsan et iusto odio dignissim qui blandit praesent luptatum zzril delenit augue duis dolore te feugait nulla facilisi.</p>
</section>
<div class="abs rule"></div>

<h2 class="abs sec-title testi-title">Client <em>Testimonials</em></h2>
<div class="abs avatar" role="img" aria-label="Portrait photo of the client"></div>
<p class="abs quote-text">Lorem ipsum dolor sit amet, consectetuer adipiscing elit, sed diam nonummy nibh euismod tincidunt ut laoreet dolore magna aliquam erat volutpat. Ut wisi enim ad minim veniam, quis nostrud exerci tation ullamcorper suscipit lobortis nisl ut aliquip ex ea commodo consequat.</p>
<div class="abs person">Daniel Hart<small>( CEO Hart &amp; Co Company )</small></div>
<a class="abs more more-t">More Details</a>

<div class="abs vline"></div>

<h2 class="abs sec-title news-title">Latest <em>News</em></h2>
<article class="abs news n1"><time>DEC 03, 2012</time><u>Lorem ipsum dolor sit amet,</u><br>consectetuer adipiscing elit, sed diam nonummy...</article>
<article class="abs news n2"><time>DEC 03, 2012</time><u>Lorem ipsum dolor sit amet,</u><br>consectetuer adipiscing elit, sed diam nonummy...</article>
<a class="abs more more-n">More Details</a>

<footer>
  <div class="abs foot-band"></div>
  <div class="abs foot-body"></div>
  <h3 class="abs col-h" style="left:75px">INSURANCE CHOICE</h3>
  <h3 class="abs col-h" style="left:350px">RESOURCES</h3>
  <h3 class="abs col-h" style="left:605px">ABOUT TOLA KOVER</h3>
  <h3 class="abs col-h" style="left:873px">FEATURED CONTENT</h3>
  <ul class="abs col" style="left:74px"><li>Auto Insurance</li><li>Local Car Insurance</li><li>Motorcycle Insurance</li><li>Commercial Auto Insurance</li><li>Life Insurance</li><li>Health Insurance</li><li>Umbrella Insurance</li></ul>
  <div class="abs sep" style="left:305px"></div>
  <ul class="abs col" style="left:351px"><li>Vehicle Resources</li><li>Insurance Basics</li><li>Articles, Blogs, and RSS</li><li>Connect with Brightlane</li><li>Mobile Apps and Services</li><li>Auto Insurance Information</li><li>KoverPerks®</li></ul>
  <div class="abs sep" style="left:553px"></div>
  <ul class="abs col" style="left:605px"><li>ABOUT BRIGHTLANE</li><li>Brightlane Overview</li><li>Jobs</li><li>Investors</li><li>Newsroom</li><li>Sponsorships</li><li>TV Commercials</li><li>Brightlane Web Sites</li></ul>
  <div class="abs sep" style="left:826px"></div>
  <ul class="abs col" style="left:875px"><li>Quote Your Way®</li><li>DriveCheck®</li><li>Pet Injury Coverage</li><li>Comparison Rates</li><li>Car Insurance Australia</li><li>Seguros para autos</li><li>Meet Our Agents</li><li>Road Trip Tales</li></ul>
  <div class="abs foot-bottom"><span>Home - Web Site Accessibility - Site Map - Help - Privacy &amp; Security - Terms of Use</span><span>Copyright 1995- 2012. TolaKover All Rights Reserved.</span></div>
</footer>

</body>
</html>
```